Velvet Lantern Tea Parlour and Sweets

Design packaging box to hold cup, saucer and wrapped food items using existing logo and theme already created by Pixel Harbor. Box needs to have a high quality look and feel. Approximate dimensions 8 inches height and 10 by 12 inches on the sides. Lid of box can be separate rather than attached.

see facebook page: https://www.examplesocial.test/velvetlanterntеaparlourandsweets

see pixel harbor projects for logos on business card and sticker:
48172093
48190526

Target Market(s)

High end Boutique

Colors
33b8a4
0355a3
f68d4e

Requirements
Must have
• color, use logo and design theme already created by pixel harbor. Want box to have design inside and outside.
Nice to have
• none to share
Should not have
• none to share

```html
<!DOCTYPE html>
<html lang="en">
<head>
<meta charset="utf-8">
<title>Velvet Lantern Tea Parlour and Sweets – Packaging Layout</title>
<link href="https://fonts.googleapis.com/css2?family=Comfortaa:wght@500&family=Quicksand:wght@400;500&family=Roboto:wght@300;400;700&display=swap" rel="stylesheet">
<style>
  :root {
    --page: #f7f7f7;
    --teal: #2eb5a2;
    --teal-soft: #8ecac1;
    --navy: #2b2a7a;
    --white: #ffffff;
    --herb-deep: #5d8a45;
    --herb-mid: #8fb870;
    --herb-light: #cfe0b4;
    --blue: #0355a3;
    --orange: #f68d4e;
    --pink: #ec8fb6;
  }
  * { box-sizing: border-box; margin: 0; padding: 0; }
  html, body { width: 1200px; height: 1200px; overflow: hidden; }
  body { background: var(--page); position: relative; font-family: "Roboto", sans-serif; }

  .card-strip { position: absolute; left: 174px; top: 218px; width: 956px; height: 319px; display: flex; }
  .card-panel { width: 319px; height: 100%; position: relative; flex: none; }
  .card-panel + .card-panel { border-left: 1px solid rgba(255,255,255,0.55); }

  .contact-panel { background: var(--teal-soft); color: var(--navy); text-align: center; }
  .contact-rule { position: absolute; left: 0; right: 0; height: 1px; background: var(--white); }
  .contact-rule.top { top: 44px; }
  .contact-rule.bottom { top: 277px; }
  .rule-mark { position: absolute; left: 151px; width: 18px; height: 18px; border-radius: 50%; background: var(--teal-soft); border: 1px solid var(--white); }
  .rule-mark.top { top: 36px; }
  .rule-mark.bottom { top: 268px; }
  .contact-name { position: absolute; top: 76px; left: 0; right: 0; font-family: "Comfortaa", sans-serif; font-weight: 500; font-size: 31px; letter-spacing: -0.5px; }
  .contact-emblem { position: absolute; top: 138px; left: 146px; width: 28px; height: 48px; border-radius: 14px 14px 3px 3px; background: rgba(255,255,255,0.4); }
  .contact-lines { position: absolute; top: 202px; left: 0; right: 0; font-family: "Quicksand", sans-serif; font-weight: 500; font-size: 17px; line-height: 21px; }

  .logo-panel { background: var(--teal); }
  .herb-wreath { position: absolute; left: 23px; top: 18px; width: 272px; height: 276px; border-radius: 28px;
    background: radial-gradient(circle at 50% 50%, var(--herb-light) 0%, var(--herb-mid) 45%, var(--herb-deep) 75%, #6d4a6e 100%); }
  .logo-disc { position: absolute; border-radius: 50%; background: var(--white); display: flex; align-items: center; justify-content: center; gap: 8px; }
  .logo-panel .logo-disc { left: 80px; top: 72px; width: 160px; height: 160px; }
  .logo-dot { width: 10px; height: 10px; border-radius: 50%; background: var(--teal); flex: none; }
  .logo-name { font-family: "Quicksand", sans-serif; font-weight: 500; color: var(--navy); font-size: 22px; line-height: 24px; text-align: left; }

  .info-panel { background: var(--teal); color: var(--white); }
  .info-title { position: absolute; left: 33px; top: 77px; font-weight: 400; font-size: 19px; letter-spacing: 2.4px; line-height: 23px; }
  .info-dash { position: absolute; left: 21px; top: 150px; width: 21px; height: 3px; background: var(--white); }
  .info-subtitle { position: absolute; left: 21px; top: 172px; font-weight: 700; font-size: 13px; letter-spacing: 2px; }
  .info-body { position: absolute; left: 21px; top: 198px; width: 270px; font-weight: 300; font-size: 14px; line-height: 17.5px; text-align: justify; }

  .box-band { position: absolute; left: 66px; top: 610px; width: 1064px; height: 356px; background: var(--white); box-shadow: 0 22px 22px -14px rgba(0,0,0,0.2); overflow: hidden; }
  .band-artwork { position: absolute; inset: 0;
    background: linear-gradient(90deg, #c9daef 0%, #e4f4f1 22%, #fbdcc8 34%, #f6d3e3 44%, #e4f4f1 56%, #f6d3e3 68%, #e4f4f1 78%, #fbdcc8 90%, #c9daef 100%); }
  .box-lid { position: absolute; left: 403px; top: 48px; width: 264px; height: 264px; background: var(--teal); }
  .box-lid .logo-disc { left: 51px; top: 51px; width: 162px; height: 162px; }
</style>
</head>
<body>
  <section class="card-strip" aria-label="Business card spread">
    <div class="card-panel contact-panel">
      <span class="contact-rule top"></span>
      <span class="rule-mark top" role="img" aria-label="Small leaf ornament"></span>
      <h1 class="contact-name">Clara Whitlow</h1>
      <span class="contact-emblem" role="img" aria-label="Line drawing of a rose stem"></span>
      <p class="contact-lines">555.014.2290<br>velvetlanterntea@example.test</p>
      <span class="contact-rule bottom"></span>
      <span class="rule-mark bottom" role="img" aria-label="Small leaf ornament"></span>
    </div>

    <div class="card-panel logo-panel">
      <div class="herb-wreath" role="img" aria-label="Watercolour wreath of herbs, purple basil and daisies"></div>
      <div class="logo-disc">
        <span class="logo-dot"></span>
        <span class="logo-name">Velvet<br>Lantern</span>
      </div>
    </div>

    <div class="card-panel info-panel">
      <h2 class="info-title">LOREM IPSUM DOLOR<br>SIT AMET</h2>
      <span class="info-dash"></span>
      <h3 class="info-subtitle">LOREM IPSUM DOLOR</h3>
      <p class="info-body">Lorem ipsum dolor sit amet, consectetuer adipiscing elit, sed diam nonummy nibh euismod tincidunt</p>
    </div>
  </section>

  <section class="box-band" aria-label="Box wrap with lid panel">
    <div class="band-artwork" role="img" aria-label="Pattern of herb and flower line drawings in blue, orange and teal with watercolour pink peonies and teal leaves"></div>
    <div class="box-lid">
      <div class="logo-disc">
        <span class="logo-dot"></span>
        <span class="logo-name">Velvet<br>Lantern</span>
      </div>
    </div>
  </section>
</body>
</html>
```